IMPROVE coffee bag design and CREATE label

I have a coffee bag design that I mostly like, but it needs some help. The colors and most of the design I like... but it needs some tweaking and I am leaving that up to your creative eye to help with ideas.
The Front: I like everything, but the coffee beans look a bit off... either arrange them better, or try different beans. I feel these may look a bit elementary in design. Also the logo at the top... there is something about the design that needs improved. Possible have the white circle closer to the logo, and have the wings sticking into the tan area.
The Back: The designer that helped me didn't seem to pay attention to small details like centering words etc.
1. the words on the back (be grateful etc.) need to be properly aligned so that each side is in alignment with the words above it.
2. The website name also isn't centered and I need a more sophisticated font for that.
3. The logo on the back, possibly needs different colors. or change the color of the other font to match logo.
Experiment to your liking, thank you.
The label for the front needs to be designed. This label needs to be customizable as it will change with different blends of coffee.
1. I do like a minimal design, but would like to incorporate a design somewhere on the label that is unique to that coffee.
Example: French Vanilla flavored coffee, would have a place for a vanilla flower... possibly a light sketch, or photo. Something minimal as not to look too cluttered. Have it designed in such a way that it can be replaced with another design for another label.
2. I would like the following on the Label.
(Coffee Name:) Sunday Lark
(Roast Level: prefer a banner, or line to indicate roast level) Med/Dark
(description) The Sunday Lark keeps you on track!
A smooth, full bodied blend of Central and South American coffee, with cupping notes of nuts and caramel.
Ingredients: 100% Arabica Beans
For the sketch or illustration on this label, please try for a sketch of lady with Sunday Lark. Some examples I've included. Please message if you have any questions.
To Clarify: I need the labels designed to be printed separately. The bag is to be designed as just a bag with the brand, very similar to what I already have posted, but with a space to put a printed Label onto the bag, as the labels will change depending on the coffee. So design label separately from bag, so it can be printed on labels and stuck to bag. Thank you
women

```html
<!DOCTYPE html>
<html lang="en">
<head>
<meta charset="utf-8">
<title>Hearth Brew – Sunday Lark Bag</title>
<link rel="stylesheet" href="https://fonts.googleapis.com/css2?family=Oswald:wght@300;400;500;700&family=Allison&family=Jost:wght@400&display=swap">
<style>
  :root {
    --backdrop: #f5dfc2;
    --silver-light: #e3e3e3;
    --silver: #c9c9c9;
    --silver-dark: #b5b5b5;
    --gold-dark: #8f7444;
    --gold: #b99361;
    --tan: #d3a466;
    --tan-light: #e3b878;
    --brown: #5a3417;
    --brown-line: #a9844f;
  }
  * { box-sizing: border-box; margin: 0; padding: 0; }
  html, body { width: 1200px; height: 800px; overflow: hidden; }
  body {
    background: var(--backdrop);
    font-family: "Oswald", sans-serif;
    color: var(--brown);
    position: relative;
  }
  .panel {
    position: absolute;
    top: 80px;
    width: 400px;
    height: 640px;
    overflow: hidden;
  }
  /* Front panel */
  .panel--front {
    left: 150px;
    background: linear-gradient(180deg, var(--silver-light) 0%, var(--silver) 60%, var(--silver-dark) 100%);
  }
  .front__band {
    position: absolute; left: 0; top: 0; width: 100%; height: 200px;
    background: linear-gradient(180deg, var(--gold-dark) 0%, var(--gold) 100%);
  }
  .brand-mark {
    position: absolute; left: 0; top: 146px; width: 100%;
    display: flex; justify-content: center; align-items: center; gap: 10px;
  }
  .brand-mark__dot {
    width: 22px; height: 22px; border-radius: 50%;
    background: var(--brown);
  }
  .brand-mark__name {
    font-weight: 500; font-size: 30px; letter-spacing: 3px;
    text-transform: uppercase; color: var(--brown);
  }
  .label {
    position: absolute; left: 30px; top: 298px; width: 340px; height: 212px;
    border: 2px solid var(--brown-line); border-radius: 10px;
    background: var(--silver-light);
    display: grid;
    grid-template-columns: 100px 1fr;
    grid-template-rows: 88px 58px 30px 1fr;
  }
  .label__art {
    grid-column: 1; grid-row: 1 / 3;
    margin: 8px; border-radius: 4px;
    background: linear-gradient(180deg, #d7d1ca 0%, #c8bcae 100%);
  }
  .label__heading {
    grid-column: 2; grid-row: 1;
    border-left: 1px solid var(--brown-line);
    border-bottom: 1px solid var(--brown-line);
    text-align: center; padding-top: 4px;
  }
  .label__name { font-weight: 700; font-size: 42px; line-height: 1; letter-spacing: -0.5px; }
  .label__motto { font-family: "Allison", cursive; font-size: 24px; line-height: 1.2; }
  .label__description {
    grid-column: 2; grid-row: 2;
    border-left: 1px solid var(--brown-line);
    font-weight: 300; font-size: 11.5px; line-height: 1.35;
    padding: 5px 8px;
  }
  .label__row {
    grid-column: 1 / 3;
    border-top: 1px solid var(--brown-line);
    display: flex; align-items: center;
  }
  .label__key { font-weight: 500; font-size: 12px; padding: 0 8px; height: 100%; display: flex; align-items: center; border-right: 1px solid var(--brown-line); }
  .label__value { font-weight: 500; font-size: 17px; padding: 0 10px; }
  .label__notes { font-weight: 300; font-size: 12px; padding: 0 10px; height: 100%; display: flex; align-items: center; border-right: 1px solid var(--brown-line); }
  .roast { display: flex; align-items: center; gap: 4px; padding-left: 8px; font-weight: 500; font-size: 12px; }
  .roast svg { display: block; }
  .front__botanical {
    position: absolute; left: 20px; top: 530px; width: 360px; height: 110px;
    background: radial-gradient(ellipse at center, rgba(211,164,102,0.18) 0%, rgba(211,164,102,0) 70%);
  }
  .front__footer {
    position: absolute; left: 0; top: 552px; width: 100%; text-align: center;
  }
  .front__lead { font-weight: 400; font-size: 14px; line-height: 1.1; }
  .front__claim { font-weight: 700; font-size: 28px; line-height: 1.05; }
  .front__weight { font-weight: 500; font-size: 13px; margin-top: 8px; }
  /* Back panel */
  .panel--back {
    left: 650px;
    background: linear-gradient(180deg, var(--silver-dark) 0%, var(--silver) 40%, var(--silver-light) 100%);
  }
  .back__pattern { position: absolute; inset: 0; }
  .back__brand {
    position: absolute; left: 158px; top: 146px;
    transform: rotate(46deg); transform-origin: left top;
    white-space: nowrap;
  }
  .back__brand-name { font-weight: 700; font-size: 36px; letter-spacing: 3px; line-height: 1; }
  .back__brand-est { font-weight: 400; font-size: 12px; letter-spacing: 2px; text-align: right; line-height: 1.2; }
  .back__mantra {
    position: absolute; left: 34px; top: 426px; width: 150px;
    font-weight: 700; line-height: 0.98; text-transform: uppercase;
  }
  .back__mantra span { display: block; white-space: nowrap; }
  .mantra__l1 { font-size: 25px; letter-spacing: 0.3px; }
  .mantra__l2 { font-size: 28px; letter-spacing: 0.6px; }
  .mantra__l3 { font-size: 28px; letter-spacing: 1px; }
  .mantra__l4 { font-size: 19.5px; letter-spacing: 0; }
  .mantra__l5 { font-size: 46px; letter-spacing: 1.2px; }
  .back__site {
    position: absolute; left: 195px; top: 576px; width: 170px; text-align: center;
    font-family: "Jost", sans-serif; font-size: 13px; letter-spacing: 0.5px;
  }
</style>
</head>
<body>
  <section class="panel panel--front">
    <div class="front__band"></div>
    <div class="brand-mark">
      <span class="brand-mark__dot"></span>
      <span class="brand-mark__name">Hearth Brew</span>
    </div>

    <article class="label">
      <div class="label__art" role="img" aria-label="Sketch illustration for the Sunday Lark blend"></div>
      <header class="label__heading">
        <h1 class="label__name">SUNDAY LARK</h1>
        <p class="label__motto">The Sunday Lark keeps you on track!</p>
      </header>
      <p class="label__description">A smooth, full bodied blend of Central and South American coffee, with cupping notes of nuts and caramel.</p>
      <div class="label__row">
        <span class="label__key">Ingredients:</span>
        <span class="label__value">100% Arabica Beans</span>
      </div>
      <div class="label__row">
        <span class="label__key">Tasting Notes:</span>
        <span class="label__notes">nuts - caramel</span>
        <span class="roast">Roast Level:
          <svg width="88" height="14" viewBox="0 0 88 14" aria-label="Roast level 4 of 5">
            <g fill="#3f2410">
              <ellipse cx="8" cy="7" rx="7" ry="5" transform="rotate(-35 8 7)"/>
              <ellipse cx="26" cy="7" rx="7" ry="5" transform="rotate(-35 26 7)"/>
              <ellipse cx="44" cy="7" rx="7" ry="5" transform="rotate(-35 44 7)"/>
              <ellipse cx="62" cy="7" rx="7" ry="5" transform="rotate(-35 62 7)"/>
            </g>
            <ellipse cx="80" cy="7" rx="7" ry="5" fill="#c9a36b" transform="rotate(-35 80 7)"/>
          </svg>
        </span>
      </div>
    </article>

    <div class="front__botanical" role="img" aria-label="Faint coffee plant branch illustration"></div>
    <footer class="front__footer">
      <p class="front__lead">BECAUSE YOU DESERVE</p>
      <p class="front__claim">BETTER COFFEE!</p>
      <p class="front__weight">NET WT. 16 oz (454g)</p>
    </footer>
  </section>

  <section class="panel panel--back">
    <svg class="back__pattern" width="400" height="640" viewBox="0 0 400 640" role="img" aria-label="Coffee bean pattern">
      <defs>
        <linearGradient id="tan-fill" x1="0" y1="0" x2="1" y2="1">
          <stop offset="0" stop-color="#c99a5c"/>
          <stop offset="1" stop-color="#e3b878"/>
        </linearGradient>
      </defs>
      <polygon points="0,150 55,132 392,512 392,640 0,640" fill="url(#tan-fill)"/>
    </svg>
    <div class="back__brand">
      <p class="back__brand-name">HEARTH BREW</p>
      <p class="back__brand-est">EST. 2023</p>
    </div>
    <p class="back__mantra">
      <span class="mantra__l1">Be Grateful</span>
      <span class="mantra__l2">Slow Down</span>
      <span class="mantra__l3">Enjoy Life</span>
      <span class="mantra__l4">Drink Delicious</span>
      <span class="mantra__l5">Coffee</span>
    </p>
    <p class="back__site">thehearthbrew.com</p>
  </section>
</body>
</html>
```